依頼詳細
「北辰年金事務研究連盟」の概要・活動内容等を紹介するパンフレットの作成です。パンフレットとはいえ、A4裏表の簡易版でOKです(ページ数2ページ)。全体として、固い厳粛なイメージが出ればよいかと思います。記載する文章等は添付ファイルのとおりですので、配置や色、デザイン等の作成をお願いします。アレンジはお任せします。
記載項目
北辰年金事務研究連盟/ごあいさつ/協議会概要/活動内容(原則、添付ファイルの通り)
サイズ
A4
ページ数
両面
希望イメージ
シンプル 複雑
単色 カラフル
暗い 明るい
日常 高級
遊び心 厳粛
未来的 伝統的
女性的 男性的
希望する色
青系、茶系、グレー系、全体のバランスがよければ必ずしも上記に拘らないです。
納品ファイル
• PNG形式 (.png)
補足説明
協議会のWEBサイトは以下です。
http://hokushin-renmei.net/
内容やイメージの参考にしてください。

やや硬いイメージを保ちつつ、シンプルで分かりやすいという点を判断基準として、選択いたしました。ありがとうございます。

この度は、多くのランサーの方からご提案いただき、大変ありがとうございます。改めて感謝申し上げます。
途中、修正依頼させていただいた方におかれましては、実際の選択ポイントからずれた内容で依頼してしまったこともあり、この点、お詫び申し上げます。(私以外の担当の意見も反映したことによるものです。何卒ご容赦ください。)
今後また案件が発生した際には、ご協力いただければ幸いです。
どうぞ宜しくお願いします。

```html
<!DOCTYPE html>
<html lang="ja">
<head>
<meta charset="utf-8">
<title>ごあいさつ｜北辰年金事務研究連盟</title>
<link rel="stylesheet" href="https://fonts.googleapis.com/css2?family=Noto+Serif+JP:wght@400;600;700;900&display=swap">
<style>
  :root {
    --band-dark: #2e2018;
    --band-mid: #4d382a;
    --band-light: #6a5040;
    --ink: #2b2522;
    --ink-soft: #3d3632;
    --rule: #b9b2ab;
    --frame: #d6d1cc;
    --paper: #ffffff;
    --header-text: #ffffff;
  }
  * { margin: 0; padding: 0; box-sizing: border-box; }
  html, body { width: 848px; height: 1200px; overflow: hidden; background: var(--paper); }
  body {
    font-family: "Noto Serif JP", serif;
    color: var(--ink);
    position: relative;
  }
  .masthead {
    position: absolute; left: 0; top: 0; width: 848px; height: 132px;
    background: linear-gradient(180deg, var(--band-light) 0%, var(--band-mid) 40%, var(--band-dark) 100%);
    color: var(--header-text);
  }
  .masthead__mark {
    position: absolute; left: 20px; top: 24px; width: 54px; height: 54px;
    background: #7a6252;
  }
  .masthead__name {
    position: absolute; left: 90px; top: 16px;
    font-size: 37px; font-weight: 700; letter-spacing: 1px; line-height: 1.2;
  }
  .masthead__tagline {
    position: absolute; left: 90px; top: 74px;
    font-size: 24px; font-weight: 700; letter-spacing: 0.5px; line-height: 1.2;
  }
  .sheet {
    position: absolute; left: 18px; top: 150px; width: 812px; height: 1030px;
    border: 1px solid var(--frame);
  }
  .greeting__title {
    position: absolute; left: 20px; top: 30px; width: 770px;
    font-size: 23px; font-weight: 600; letter-spacing: 2px;
    padding-bottom: 12px; border-bottom: 1px solid var(--rule);
  }
  .greeting__body {
    position: absolute; left: 22px; top: 110px; width: 766px;
    font-size: 13.5px; line-height: 27px; color: var(--ink-soft);
  }
  .greeting__body p { margin-bottom: 27px; text-indent: 1em; }
  .greeting__body p.lead { text-indent: 0; }
  .signature {
    position: absolute; right: 40px; top: 900px; text-align: right;
    color: var(--ink-soft);
  }
  .signature__org { font-size: 14px; margin-bottom: 4px; }
  .signature__rep { font-size: 14px; }
  .signature__rep strong { font-size: 21px; font-weight: 600; margin-left: 10px; letter-spacing: 2px; }
</style>
</head>
<body>
  <header class="masthead">
    <div class="masthead__mark"></div>
    <h1 class="masthead__name">北辰年金事務研究連盟</h1>
    <p class="masthead__tagline">社保調査の専門家「社会保険労務士」による全国組織</p>
  </header>

  <main class="sheet">
    <h2 class="greeting__title">ごあいさつ</h2>
    <div class="greeting__body">
      <p class="lead">北辰年金事務研究連盟／代表の柏木でございます。</p>
      <p>昨今、厚生労働省（日本年金機構）による、社会保険の取り締まりが一段と厳しさを増しております。具体的には、法人でありながら社会保険に加入していない、いわゆる“加入漏れ”、あるいは社会保険には加入しているが、対象者全員を加入させていない、いわゆる“加入漏れ”――こういった企業に対する取り締まりが強化されています。</p>
      <p>当然ではありますが、今後は、中小規模の企業様におかれましても、社会保険に適正に加入することを前提として、経営を考えていかなければならないといえるでしょう。</p>
      <p>このような問題を踏まえ、我々開業社会保険労務士がチームを組み、社会保険への適正加入の促進活動を行なっていくことを目的として、この度、「北辰年金事務研究連盟」を設立させていただいた次第でございます。</p>
      <p>ただ、一方で社会保険の負担が非常に重いという問題もありますので、その中で、「いかにして負担を軽減しながら、適正に社会保険に加入することができるのか」という視点に立ち、企業経営者の方とともに解決策を探っていくアドバイザー的な役割として、各種サービスをご提供させていただければと考えております。</p>
      <p>今後、当連盟の活動にご期待ください。今後ともどうぞよろしくお願い申し上げます。</p>
    </div>
    <div class="signature">
      <p class="signature__org">北辰年金事務研究連盟</p>
      <p class="signature__rep">代表<strong>柏木遼一</strong></p>
    </div>
  </main>
</body>
</html>
```